Business Card Design

BrambleWick Kitchen is the name of my health coaching business. My tag line is "Where good health meets real life." I will be working with clients one-on-one and in groups. My target clients are women "of a certain age" who want to be more comfortable in their own skin. We will work together in a 6-month program. The coaching sessions will take place in my kitchen. I will also be conducting monthly cooking classes and field trips - to farmer's markets, speciality markets etc.. for my clients.
Updates

the business name is BrambleWick Kitchen - I'm not sure how the p got in there at the end of the name

Thank you

Please include the website - www.bramblewickkitchen.example and the tag line:

Where good health meets real life on the business card.

Thank you

Please add the phone number to the business card - sorry, I forgot to state that in the original brief

(555) 802-4716

Target Market(s)

Women "of a certain age" who want to be more comfortable in their own skin

Industry/Entity Type

Cooking

Contact Information for Business Card

BrambleWick Kitchen
Where good health meets real life

Doreen Ashworth
Health Coach
(555) 802-4716

Font styles to use
Serif
Sans Serif

Requirements
Must have
• front & back design
I typical like soft colors - and have tended toward greens over time - I'm open although I would not like bright reds, yellows etc..

```html
<!DOCTYPE html>
<html lang="en">
<head>
<meta charset="utf-8">
<title>BrambleWick Kitchen – Business Card</title>
<link rel="stylesheet" href="https://fonts.googleapis.com/css2?family=Maven+Pro:wght@400;500&display=swap">
<style>
  :root {
    --leaf: #7bc043;
    --ink: #333333;
    --paper: #ffffff;
    --backdrop-light: #f6f6f6;
    --backdrop-dark: #dedede;
    --edge: #1a1a1a;
  }
  * { box-sizing: border-box; margin: 0; padding: 0; }
  html, body { width: 1200px; height: 900px; overflow: hidden; }
  body {
    position: relative;
    background: linear-gradient(200deg, var(--backdrop-light) 0%, var(--backdrop-dark) 100%);
    font-family: "Maven Pro", sans-serif;
    color: var(--ink);
  }
  .card {
    position: absolute;
    width: 716px;
    height: 388px;
    background: var(--paper);
    border: 1px solid var(--edge);
    overflow: hidden;
  }
  .card--front { left: 110px; top: 22px; }
  .card--back { left: 315px; top: 448px; }

  .business-name {
    position: absolute;
    font-family: "Maven Pro", sans-serif;
    font-weight: 500;
    font-size: 34px;
    line-height: 1;
    color: var(--ink);
    white-space: nowrap;
  }
  .tagline {
    position: absolute;
    font-family: "Maven Pro", sans-serif;
    font-weight: 400;
    font-size: 15px;
    line-height: 1;
    color: var(--ink);
    white-space: nowrap;
  }
  .card--front .business-name { left: 66px; top: 52px; }
  .card--front .tagline { left: 67px; top: 100px; }

  .person {
    position: absolute;
    top: 206px;
    font-size: 21px;
    font-weight: 500;
    color: var(--leaf);
    white-space: nowrap;
  }
  .person--name { left: 66px; }
  .person--role { right: 62px; }

  .rule {
    position: absolute;
    left: 0; right: 0;
    height: 1px;
    background: var(--leaf);
  }
  .rule--top { top: 233px; }
  .rule--bottom { top: 343px; }

  .contact-band {
    position: absolute;
    left: 0; right: 0;
    top: 237px;
    height: 104px;
    background: var(--leaf);
    color: var(--paper);
  }
  .contact {
    position: absolute;
    display: flex;
    align-items: center;
    gap: 12px;
    font-size: 19px;
    white-space: nowrap;
  }
  .contact svg { flex: none; }
  .contact--social { left: 66px; top: 21px; }
  .contact--phone { left: 66px; top: 61px; gap: 10px; }
  .contact--email { left: 300px; top: 22px; }
  .contact--web { left: 300px; top: 61px; }

  .card--front .footer-url {
    position: absolute;
    left: 0; right: 0;
    top: 356px;
    text-align: center;
    font-size: 17px;
    color: var(--ink);
  }

  .back-band {
    position: absolute;
    left: 0; right: 0;
    background: var(--leaf);
    color: var(--paper);
  }
  .back-band--top { top: 0; height: 122px; }
  .back-band--bottom { top: 260px; bottom: 0; }
  .promise {
    position: absolute;
    left: 0; right: 0;
    top: 82px;
    text-align: center;
    font-size: 18px;
    white-space: nowrap;
  }
  .card--back .business-name { left: 0; right: 0; top: 170px; text-align: center; }
  .card--back .tagline { left: 0; right: 0; top: 216px; text-align: center; }
  .card--back .footer-url {
    position: absolute;
    left: 0; right: 0;
    top: 88px;
    text-align: center;
    font-size: 17px;
  }
</style>
</head>
<body>

  <section class="card card--front" aria-label="Business card front">
    <div class="business-name">BrambleWick Kitchen</div>
    <div class="tagline">Where good health meets real life</div>

    <div class="person person--name">Doreen Ashworth</div>
    <div class="person person--role">Health Coach</div>

    <div class="rule rule--top"></div>
    <div class="contact-band">
      <div class="contact contact--social">
        <svg width="22" height="22" viewBox="0 0 22 22" aria-hidden="true"><circle cx="11" cy="11" r="11" fill="#ffffff"/></svg>
        <span>bw_kitchen</span>
      </div>
      <div class="contact contact--phone">
        <svg width="12" height="20" viewBox="0 0 12 20" aria-hidden="true"><path d="M3 2 Q8 2 8 10 Q8 18 3 18 L3 15 Q5 15 5 10 Q5 5 3 5 Z" fill="#ffffff"/></svg>
        <span>(555) 802-4716</span>
      </div>
      <div class="contact contact--email">
        <svg width="22" height="16" viewBox="0 0 22 16" aria-hidden="true"><rect x="1" y="1" width="20" height="14" fill="none" stroke="#ffffff" stroke-width="2"/><path d="M1 1 L11 9 L21 1" fill="none" stroke="#ffffff" stroke-width="2"/></svg>
        <span>doreen@bramblewickkitchen.example</span>
      </div>
      <div class="contact contact--web">
        <svg width="22" height="22" viewBox="0 0 22 22" aria-hidden="true"><g fill="none" stroke="#ffffff" stroke-width="1.5"><circle cx="11" cy="11" r="9.5"/><ellipse cx="11" cy="11" rx="4" ry="9.5"/><path d="M1.5 11 H20.5 M3 6 H19 M3 16 H19"/></g></svg>
        <span>www.bramblewickkitchen.example</span>
      </div>
    </div>
    <div class="rule rule--bottom"></div>

    <div class="footer-url">www.bramblewickkitchen.example</div>
  </section>

  <section class="card card--back" aria-label="Business card back">
    <div class="back-band back-band--top">
      <p class="promise">Reach your Health and weight loss goals with a plan designed just for you</p>
    </div>
    <div class="business-name">BrambleWick Kitchen</div>
    <div class="tagline">Where good health meets real life</div>
    <div class="back-band back-band--bottom">
      <div class="footer-url">www.bramblewickkitchen.example</div>
    </div>
  </section>

</body>
</html>
```